Zielgruppe
Wir sind KQ Rapid Voltwerk GmbH mit Sitz in Basel Schweiz. Wir bieten die volle Palette von Elektronikdienstleistungen. Besonders aber Photovoltaik (Solar) auf Einfamilienhäusern und Gewerbeeinheiten, Smart Home Automation mit Dravix (Partner) und allgemeine Elektrikerdienstleistungen in Häusern und Wohnung.
USP
• Regionale Firma, BS, BL,AG
○ Daher schnelle Reaktion im Störungsfall. Garantierte Entstörung
• Umsetzung innert 2-3 Monate
• Planung und Durchführung aus einer Hand.
• Umsetzung auch in der PV Installation nur durch eigene Mitarbeiter
• Kelmora Förderung, bis zu 6TCHF
• Kompetent, freundlich
• Eidgenössich diplomierter Elektroinstallateur (Meister)
• EFZ (Eidgenösisch Fährigkeitszeugnis)
• 1 Jahr Existenz
• Dravix goldpartner
• Nur Doppelglasmodule mit 25 Jahre Garantie, 10 Jahre auf Wechselrichter und Batterie
• Planung mittels CAD/*D Planung, technische Tool
• Genaues und schnelles Angebot innert 5 Werktagen
USP:
• Stromkosten sparen
• Autark werden, unabhängig von Strompreisentwicklung
• Umwelt schützen
WUNSCHKUNDE
• Soziodemografisch
○ Eigentümer
○ Gehobene Mittelklasse
• Lokalität in Basel und Umgebung
Aufgabenstellung
Medien unter: https://files.trobelix.ch/index.php/s/mQzWnLpRtYvA7KD
Logo ist dort vorhanden.
Hintergrund hell (weiss, hellgrau bspw.)
Schriftart
Verlinkungen zu Social Media:
• Facebook
• Linkedin
• Instagram
Beispielseiten, die gefallen:
Alpin Lichtfeld Werk (alpin-lichtfeld-werk.ch) Prio
Counter mit

```html
<!DOCTYPE html>
<html lang="de">
<head>
<meta charset="utf-8">
<title>KQ Rapid Voltwerk GmbH – Offene Stellen</title>
<link href="https://fonts.googleapis.com/css2?family=Poppins:wght@400;500;600;700;800&family=Montserrat:wght@600;700&family=Bebas+Neue&family=Playfair+Display:wght@600&family=Open+Sans:ital,wght@0,400;1,300;1,400&display=swap" rel="stylesheet">
<style>
:root{
  --green:#0a9452;
  --green-dark:#0b6b3a;
  --green-soft:#3dae7c;
  --hero-green:#5fbd93;
  --yellow:#f6d21e;
  --lime:#8bd66a;
  --ink:#222;
  --muted:#888;
  --line:#e2e2e2;
  --blue:#2e6fb7;
}
*{box-sizing:border-box;margin:0;padding:0}
html,body{width:1200px;height:2263px;overflow:hidden;background:#fff;font-family:"Poppins",sans-serif;color:var(--ink)}
.page{position:relative;width:1200px;height:2263px}
.abs{position:absolute}

/* top bar */
.topbar{top:18px;left:88px;font-size:14px;color:#444;display:flex;gap:22px;align-items:center}
.topbar span{display:flex;align-items:center;gap:8px}
.topbar .mail{font-size:11px;text-decoration:underline}
.social-top{top:24px;right:84px;display:flex;gap:10px;align-items:center;font-size:11px;color:#333;font-weight:500}
.sq{width:15px;height:15px;border-radius:3px;display:inline-block}

/* header */
.brand{top:66px;left:84px;display:flex;align-items:center;gap:10px}
.brand .dot{width:44px;height:44px;border-radius:50%;background:var(--green)}
.brand .name{font-size:18px;line-height:21px;color:var(--green-dark);font-weight:500;width:130px}
.nav{top:86px;left:384px;display:flex;gap:32px;font-family:"Montserrat",sans-serif;font-size:18px;letter-spacing:1.8px;font-weight:600}
.nav .active{color:var(--green)}
.nav a{color:#1f3b2a;text-decoration:none}
.nav .plus{font-size:22px;margin-left:-14px;color:#222}
.btn-kontakt{top:78px;left:1011px;width:104px;height:44px;background:var(--green-dark);color:#fff;border-radius:5px;font-weight:700;font-size:17px;display:flex;align-items:center;justify-content:center;letter-spacing:.5px}
.header-line{top:152px;left:0;width:1200px;height:2px;background:#cfe8db}

/* hero */
.hero{top:154px;left:0;width:1200px;height:301px;background:linear-gradient(100deg,#56b488,#7cc9a4 60%,#63bb92)}
.hero-title{top:198px;left:90px;font-size:35px;font-weight:800;color:var(--yellow);letter-spacing:.3px}
.hero-text{top:254px;left:90px;width:1030px;font-size:18px;line-height:26.5px;color:#fff}

.job{width:298px;height:422px;border-radius:26px;border:4px solid #fff;overflow:hidden;box-shadow:0 2px 8px rgba(0,0,0,.08)}
.job .photo{width:100%;height:100%;background:linear-gradient(160deg,#8f8f8a,#3a3b38 70%)}
.job .label{position:absolute;left:0;right:0;bottom:0;background:rgba(11,120,68,.88);color:#fff;font-weight:700;font-size:21px;line-height:32px;text-align:center;display:flex;align-items:center;justify-content:center;border-radius:22px 22px 0 0}
.job1{top:375px;left:552px}
.job1 .label{height:156px;padding-top:6px}
.job2{top:375px;left:868px}
.job2 .photo{background:linear-gradient(160deg,#bdbab2,#45453f 70%)}
.job2 .label{height:146px;left:6px}

/* testimonials */
.section-title{top:856px;left:0;width:1200px;text-align:center;font-size:32px;font-weight:800;color:var(--green)}
.tcard{background:#fff;border-radius:14px;box-shadow:0 4px 10px rgba(0,0,0,.12)}
.tcard.main{top:948px;left:364px;width:484px;height:268px}
.tcard.side-l{top:940px;left:-20px;width:313px;height:262px}
.tcard.side-r{top:936px;left:936px;width:300px;height:262px}
.quote-mark{font-family:"Poppins",sans-serif;font-weight:800;color:var(--green);font-size:70px;line-height:1}
.tcard p{font-size:14px;line-height:21px;text-align:center}
.side-l p,.side-r p{color:#555;font-size:14px}
.avatar{border-radius:50%;background:linear-gradient(160deg,#c9c9c4,#3f403b);border:2px solid #fff;box-shadow:0 0 0 1px #333}
.pname{font-weight:700;font-size:18px}
.prole{font-size:19px}
.arrow{width:46px;height:46px;border-radius:50%;background:#fff;box-shadow:0 3px 6px rgba(0,0,0,.2);display:flex;align-items:center;justify-content:center}

/* form */
.form-title{top:1270px;left:101px;font-family:"Playfair Display",serif;font-size:34px;font-weight:600;color:#1d2a28}
.form-rule{top:1321px;left:101px;width:89px;height:2px;background:var(--blue)}
.form-hint{top:1346px;left:101px;font-family:"Open Sans",sans-serif;font-style:italic;font-weight:300;font-size:15px;color:#999}
.lbl{font-family:"Open Sans",sans-serif;font-style:italic;font-weight:400;font-size:14px;color:#444}
.field{height:46px;border:1px solid var(--line);background:#fff;font-family:"Open Sans",sans-serif;font-size:14px;color:#888;padding:0 14px;display:flex;align-items:center}
.field.focus{border-color:var(--blue);color:#333;font-style:italic}
.radio{display:flex;align-items:center;gap:8px;font-family:"Open Sans",sans-serif;font-style:italic;font-size:14px;color:#444}
.radio i{width:15px;height:15px;border:1.5px solid #333;border-radius:50%;display:inline-block}
.send{top:1809px;left:93px;width:554px;height:52px;border-radius:26px;background:var(--green);color:#fff;font-weight:600;font-size:18px;letter-spacing:.5px;display:flex;align-items:center;justify-content:center}

.contact-panel{top:1272px;left:673px;width:522px;height:589px;border-radius:42px 0 0 0;background:linear-gradient(160deg,#3aae7d,#2fa470 55%,#27a068)}
.panel-rule{top:1300px;left:697px;width:61px;height:4px;background:#0d3b25}
.panel-eyebrow{top:1319px;left:693px;font-size:17px;font-weight:700;letter-spacing:1.6px;color:#fff}
.panel-head{top:1352px;left:693px;font-family:"Bebas Neue",sans-serif;font-size:41px;color:#fff;letter-spacing:.3px}
.panel-sub{top:1403px;left:693px;width:450px;font-size:18px;font-weight:700;line-height:26px;color:#fff}
.panel-addr{top:1573px;left:765px;font-size:18px;font-weight:500;line-height:26px;color:#fff}

/* footer */
.footer{top:1938px;left:0;width:1200px;height:286px;background:var(--green)}
.f-brand{top:1982px;left:85px;display:flex;align-items:center;gap:10px;color:#fff}
.f-brand .dot{width:42px;height:42px;border-radius:50%;background:#fff}
.f-brand .name{font-size:17px;line-height:20px;width:120px;font-weight:500}
.f-head{top:1974px;left:273px;font-size:15px;font-weight:700;line-height:24px;color:#fff}
.f-body{top:2037px;left:273px;width:270px;font-size:14px;line-height:21px;color:#fff}
.f-social{top:2170px;left:273px;display:flex;gap:11px}
.f-social span{width:24px;height:24px;background:#111;display:inline-block}
.f-social span.y{background:#d9b84a}
.partner{top:2040px;left:582px;font-size:48px;font-weight:600;color:var(--lime);letter-spacing:1px}
.f-abo{top:1967px;left:784px;font-family:"Open Sans",sans-serif;font-style:italic;font-size:22px;font-weight:300;color:#fff}
.f-abo-rule{top:2011px;left:784px;width:70px;height:2px;background:#e8c66a}
.f-input{top:2045px;left:784px;width:329px;height:49px;background:#fff;display:flex;align-items:center;gap:10px;padding-left:12px;font-size:14px;color:#777;font-family:"Open Sans",sans-serif}
.f-input .sep{width:1px;height:22px;background:#ccc}
.f-note{top:2119px;left:784px;width:330px;font-family:"Open Sans",sans-serif;font-style:italic;font-size:13.5px;line-height:19px;color:#fff}
.copy{top:2233px;left:0;width:1200px;text-align:center;font-size:14.5px;color:var(--green)}
</style>
</head>
<body>
<div class="page">

  <div class="abs topbar">
    <span><svg width="16" height="16" viewBox="0 0 24 24"><path fill="#0a9452" d="M6.6 10.8a15 15 0 0 0 6.6 6.6l2.2-2.2c.3-.3.7-.4 1-.2 1.1.4 2.3.6 3.6.6.6 0 1 .4 1 1V20c0 .6-.4 1-1 1A17 17 0 0 1 3 4c0-.6.4-1 1-1h3.5c.6 0 1 .4 1 1 0 1.3.2 2.5.6 3.6.1.3 0 .7-.2 1z"/></svg>+41 61 555 0187</span>
    <span class="mail"><svg width="18" height="14" viewBox="0 0 24 18"><rect x="1" y="1" width="22" height="16" rx="2" fill="#0a9452"/><path d="M2 2l10 8 10-8" stroke="#fff" stroke-width="2" fill="none"/></svg>kontakt@kqrapid.ch</span>
  </div>
  <div class="abs social-top">Social Media:
    <i class="sq" style="background:#2f5da8"></i><i class="sq" style="background:#d8407a"></i><i class="sq" style="background:#1f66a8"></i><i class="sq" style="background:#111"></i>
  </div>

  <div class="abs brand"><div class="dot"></div><div class="name">KQ Rapid Voltwerk GmbH</div></div>
  <nav class="abs nav"><a class="active">Homepage</a><a>Referenzen</a><a>Dienstleistungen</a><span class="plus">+</span></nav>
  <div class="abs btn-kontakt">KONTAKT</div>
  <div class="abs header-line"></div>

  <div class="abs hero" role="img" aria-label="Grün eingefärbtes Teamfoto einer Besprechung"></div>
  <h1 class="abs hero-title">UNSERE OFFENEN STELLEN</h1>
  <p class="abs hero-text">Wir Haben Deine Interesse Geweckt?<br>Du Willst In Unserem Jungen Unternehmen Und Team Fuß Fassen Und Jemand Sein? Dann Schau Dir Unsere Offenen Stellen An Und Schick Uns Deine Bewerbung Oder Ruf Uns Einfach Mal An.<br>Lass Uns Gemeinsam Richtig Durchstarten!</p>

  <div class="abs job job1"><div class="photo" role="img" aria-label="Elektroniker arbeitet an einem Schaltschrank mit Laptop"></div><div class="label">ELEKTRONIKER FÜR<br>ENERGIE- UND<br>GEBÄUDETECHNIK</div></div>
  <div class="abs job job2"><div class="photo" role="img" aria-label="Elektrohelfer im Firmenshirt vor einer Tür"></div><div class="label">ELEKTROHELFER</div></div>

  <h2 class="abs section-title">MITARBEITERZITAT</h2>

  <div class="abs tcard side-l">
    <p class="abs" style="top:32px;left:0;width:300px;text-align:left;line-height:21px">Und Lenz Waren Ein Wichtiger Baustein<br>res Projektoffices VELMATO. Nach Einem<br>Timo Und Lenz Sofort Die Problemstellung<br>nden Problemen, Brachten Sie Direkt<br>he Lösungsalternativen.</p>
    <div class="abs pname" style="top:172px;left:0;color:#555">co Birrer</div>
    <div class="abs prole" style="top:198px;left:0;color:#555">MATO.Com</div>
  </div>
  <div class="abs quote-mark" style="top:918px;left:-12px">”</div>

  <div class="abs tcard main">
    <p class="abs" style="top:30px;left:28px;width:430px">DasArbeitsklima Unter Den Kollegen Ist Super, Man Hat Immer Was Zu Lachen. Dieselbstständige Arbeitsweise Und Das Vertrauen In Meine Arbeit Schätze Ich Sehr.Bei KQ Rapid Läuft Sehr Vieles Digital, Was Ich Auch Sehr Gut Finde“</p>
    <div class="abs avatar" style="top:152px;left:32px;width:90px;height:90px" role="img" aria-label="Porträt eines Mitarbeiters"></div>
    <div class="abs pname" style="top:173px;left:138px">Lenz</div>
    <div class="abs prole" style="top:199px;left:140px">Mitarbeiter</div>
  </div>
  <div class="abs quote-mark" style="top:913px;left:602px">”</div>
  <div class="abs quote-mark" style="top:893px;left:1155px;color:#7fcfa5">”</div>
  <div class="abs arrow" style="top:1055px;left:340px"><svg width="16" height="16" viewBox="0 0 16 16"><path d="M11 2L5 8l6 6" stroke="#0a9452" stroke-width="2.5" fill="none"/></svg></div>
  <div class="abs arrow" style="top:1055px;left:824px"><svg width="16" height="16" viewBox="0 0 16 16"><path d="M5 2l6 6-6 6" stroke="#0a9452" stroke-width="2.5" fill="none"/></svg></div>

  <div class="abs tcard side-r">
    <p class="abs" style="top:30px;left:18px;width:300px;line-height:21px">KQ Rapid Und Insbesondere Lenz W<br>Bei Der Realisierungunseres Projekt<br>Initialgespräch War Timo Und Lenz<br>Klar Und Bei Auftretenden Prob<br>Mögliche Lösungs</p>
    <div class="abs avatar" style="top:144px;left:18px;width:92px;height:92px;box-shadow:none" role="img" aria-label="Porträt eines Kunden"></div>
    <div class="abs pname" style="top:166px;left:138px;color:#555">Marco Birr</div>
    <div class="abs prole" style="top:192px;left:140px;color:#555">Mitarbeiter</div>
  </div>

  <h2 class="abs form-title">Rückruf-Formular</h2>
  <div class="abs form-rule"></div>
  <div class="abs form-hint">gewünschter Rückruf-Zeitpunkt</div>

  <div class="abs lbl" style="top:1389px;left:97px">Vorname</div>
  <div class="abs field" style="top:1415px;left:93px;width:263px">Enter your&nbsp; Vorname</div>
  <div class="abs lbl" style="top:1389px;left:383px">Nachname</div>
  <div class="abs field" style="top:1415px;left:383px;width:264px">Enter your nachname</div>

  <div class="abs lbl" style="top:1486px;left:93px">Mail</div>
  <div class="abs field focus" style="top:1512px;left:93px;width:263px">John.exp@gm</div>
  <div class="abs lbl" style="top:1486px;left:383px">Telefon</div>
  <div class="abs field" style="top:1512px;left:383px;width:264px">telefon</div>

  <div class="abs lbl" style="top:1583px;left:93px">Gelernter Elektriker</div>
  <div class="abs radio" style="top:1612px;left:101px"><i></i>ja</div>
  <div class="abs radio" style="top:1638px;left:101px"><i></i>nein</div>
  <div class="abs lbl" style="top:1583px;left:383px">Berufserfahrung in Jahren</div>
  <div class="abs field" style="top:1609px;left:383px;width:264px"></div>

  <div class="abs lbl" style="top:1680px;left:93px">Kommentar</div>
  <div class="abs field" style="top:1706px;left:93px;width:554px;height:70px;align-items:flex-start;padding-top:14px">Kommentar</div>
  <div class="abs send">SENDEN</div>

  <div class="abs contact-panel" role="img" aria-label="Grün eingefärbtes Foto einer Kundenberaterin mit Headset"></div>
  <div class="abs panel-rule"></div>
  <div class="abs panel-eyebrow">IHRE ANLIEGEN IM FOKUS</div>
  <div class="abs panel-head">WIR FREUEN UNS VON IHNEN ZU HÖREN!</div>
  <div class="abs panel-sub">Sie Benötigen Unterstützung? Nehmen Sie Jetzt Kontakt Mit Uns Auf!</div>
  <svg class="abs" style="top:1576px;left:697px" width="32" height="42" viewBox="0 0 32 42"><path d="M16 0C7 0 0 7 0 16c0 11 16 26 16 26s16-15 16-26C32 7 25 0 16 0z" fill="#fff"/></svg>
  <div class="abs panel-addr">KQ Rapid Voltwerk GmbH<br>Im Feldacker 12<br>CH-4053 Basel</div>

  <footer class="abs footer"></footer>
  <div class="abs f-brand"><div class="dot"></div><div class="name">KQ Rapid Voltwerk GmbH</div></div>
  <div class="abs f-head">ELEKTRONIK FÜR EINE<br>STRAHLENDE ZUKUNFT</div>
  <p class="abs f-body">Innovative Technologie, Umweltfreundliche Elektronik: Ihr Zuhause Wird Lebendig Mit Unseren Lösungen Für Eine Grüne, Nachhaltige Zukunft.</p>
  <div class="abs f-social"><span></span><span class="y"></span><span></span><span></span></div>
  <div class="abs partner">DRAVIX</div>
  <div class="abs f-abo">Abonnieren</div>
  <div class="abs f-abo-rule"></div>
  <div class="abs f-input"><svg width="18" height="18" viewBox="0 0 24 24"><rect x="3" y="5" width="18" height="14" rx="3" fill="none" stroke="#e2b865" stroke-width="1.6"/><path d="M6 9l6 4 6-4" fill="none" stroke="#e2b865" stroke-width="1.6"/></svg><i class="sep"></i>Geben sie ihre E-Mail Adresse ein</div>
  <p class="abs f-note">Senden Sie eine E-Mail und Sie erhalten regelmäßig unsere Newsletter, Service-Blogs und Pressemitteilungen</p>
  <div class="abs copy">Copyright 2024 KQ Rapid Voltwerk GmbH, All Right Reserved</div>

</div>
</body>
</html>
```